Hip and quirky Indian restaurant Menu

We need a build your own bowl/meal/wrap menu similar to Verdigo others. We would like illustrations if possible of India/veggies/chicken/animals/themes. Please utilize the colors that match the schema of the logos provided. We have included pictures you may use them if you would like to. Menu provided is our old menu.

Target Market(s)

Millenials, Ge

Industry/Entity Type

Retail

Font styles to use
Sans Serif
Decorative

Requirements
Must have
• logical placements for build your own meal options
Nice to have
• Illustrations.

```html
<!DOCTYPE html>
<html lang="en">
<head>
<meta charset="utf-8">
<title>Saffron Lane – Menu</title>
<link rel="stylesheet" href="https://fonts.googleapis.com/css2?family=Fjalla+One&family=Montserrat:wght@400;500;700;800;900&family=Caveat+Brush&family=Kaushan+Script&display=swap">
<style>
  :root {
    --orange: #f26b2a;
    --navy: #2b2a6b;
    --red: #e8232f;
    --ink: #231815;
    --peach: #fbd9a8;
    --paper: #ffffff;
  }
  * { margin: 0; padding: 0; box-sizing: border-box; }
  html, body { width: 1200px; height: 848px; overflow: hidden; background: var(--paper); }
  .menu { position: relative; width: 1200px; height: 848px; color: var(--ink); font-family: "Montserrat", sans-serif; overflow: hidden; }
  .abs { position: absolute; }

  /* Build your own */
  .build-panel { left: 0; top: 0; width: 362px; height: 540px; }
  .build-title { left: 38px; top: 52px; color: var(--paper); font-family: "Fjalla One", sans-serif; line-height: .95; font-weight: 400; }
  .build-title .line1 { font-size: 33px; display: block; }
  .build-title .line2 { font-size: 56px; display: block; margin-left: 14px; }
  .ribbon { left: 10px; top: 136px; width: 200px; height: 60px; }
  .build-title .script { position: absolute; left: 8px; top: 86px; font-family: "Kaushan Script", cursive; color: var(--ink); font-size: 48px; white-space: nowrap; }
  .price-disc { left: 209px; top: 60px; width: 118px; height: 118px; border-radius: 50%; background: var(--paper); display: flex; align-items: center; justify-content: center; }
  .price { font-family: "Caveat Brush", cursive; font-size: 42px; line-height: 1; }
  .price-disc .price { color: var(--ink); }
  .step { left: 37px; width: 300px; color: var(--paper); }
  .step h3 { font-size: 12px; font-weight: 800; letter-spacing: .2px; margin-bottom: 11px; }
  .step p { font-size: 8.3px; line-height: 1.25; font-weight: 500; }
  .step .extras { display: flex; gap: 22px; margin-top: 7px; }
  .step .note { font-size: 5px; margin-left: 156px; margin-top: 3px; }

  /* Brand */
  .brand-backdrop { left: 436px; top: 28px; width: 330px; height: 330px; border-radius: 50%; background: radial-gradient(circle, rgba(251,217,168,.75) 0%, rgba(251,217,168,.45) 55%, rgba(251,217,168,0) 72%); }
  .brand { left: 430px; top: 80px; width: 340px; text-align: center; font-family: "Fjalla One", sans-serif; font-size: 96px; color: var(--navy); line-height: 1.02; }

  /* Feature bowl */
  .feature-title { left: 406px; top: 386px; font-family: "Fjalla One", sans-serif; font-weight: 400; font-size: 31px; line-height: 1; }
  .feature-price { left: 716px; top: 384px; color: var(--ink); font-size: 40px; }
  .feature-quote { left: 393px; top: 442px; width: 220px; text-align: center; font-size: 12.5px; line-height: 1.2; }
  .feature-serve { left: 393px; top: 506px; width: 220px; text-align: center; font-size: 8px; }
  .hatch { left: 404px; top: 538px; width: 240px; height: 24px; }
  .photo-bowl { left: 612px; top: 433px; width: 248px; height: 150px; border-radius: 50%; background: radial-gradient(ellipse at center, #d99a2e 0%, #c9a64e 45%, #e9e6e1 62%, #f3f2f0 100%); }
  .photo-snack { left: 1035px; top: -10px; width: 200px; height: 166px; border-radius: 50%; background: radial-gradient(ellipse at 70% 45%, #c98a3a 0%, #d9a55a 30%, #ececea 55%, #f6f6f5 100%); }

  /* Lists */
  .section-head { font-family: "Fjalla One", sans-serif; font-weight: 400; line-height: 1; }
  .list { list-style: none; font-weight: 800; font-size: 12px; }
  .list li { position: relative; height: 27px; white-space: nowrap; }
  .list .amt { position: absolute; font-weight: 500; font-size: 10px; top: 1px; }

  .snacks-head { left: 860px; top: 56px; font-size: 44px; }
  .swash { left: 866px; top: 108px; width: 110px; height: 28px; }
  .snacks { left: 903px; top: 157px; width: 250px; }
  .snacks .amt { left: 188px; }

  .fries-band { left: 861px; top: 332px; width: 316px; height: 62px; background: var(--navy); color: var(--paper); display: flex; align-items: center; justify-content: center; font-family: "Fjalla One", sans-serif; font-weight: 400; font-size: 39px; font-style: italic; }
  .fries { left: 902px; top: 426px; }
  .fries-disc { left: 1068px; top: 413px; width: 84px; height: 84px; border-radius: 50%; background: var(--navy); color: var(--paper); display: flex; align-items: center; justify-content: center; }
  .fries-disc .price { font-size: 26px; }

  .drinks-head { left: 978px; top: 534px; font-family: "Montserrat", sans-serif; font-weight: 900; font-size: 42px; line-height: 1; }
  .drinks-a { left: 839px; top: 591px; width: 150px; }
  .drinks-a .amt { left: 137px; }
  .drinks-b { left: 1024px; top: 591px; width: 130px; }
  .drinks-b .amt { left: 121px; }

  .desserts-head { left: 955px; top: 686px; font-family: "Kaushan Script", cursive; font-weight: 400; font-size: 44px; line-height: 1.1; }
  .desserts { left: 902px; top: 756px; width: 250px; }
  .desserts .amt { left: 188px; }

  .lassi-head { left: 107px; top: 564px; font-size: 33px; }
  .lassi-cols { left: 256px; top: 623px; font-weight: 800; font-size: 11px; }
  .lassi-cols span { position: absolute; }
  .lassi { left: 37px; top: 647px; width: 300px; }
  .lassi .s { left: 215px; }
  .lassi .l { left: 273px; }

  .meals-head { left: 450px; top: 598px; width: 300px; text-align: center; font-weight: 400; }
  .meals-head .script { display: block; font-family: "Kaushan Script", cursive; font-size: 44px; line-height: 1; }
  .meals-head .block { display: block; font-weight: 900; font-size: 43px; line-height: 1; margin-top: 2px; }
  .rays { left: 448px; top: 610px; width: 304px; height: 80px; }
  .meals { left: 456px; top: 729px; }
  .meals-disc { left: 689px; top: 694px; width: 116px; height: 116px; border-radius: 50%; background: var(--red); color: var(--paper); display: flex; align-items: center; justify-content: center; }
  .meals-disc .price { font-size: 36px; }

  .stroke { fill: none; stroke: var(--ink); stroke-linecap: round; }
</style>
</head>
<body>
<main class="menu">

  <svg class="abs build-panel" viewBox="0 0 362 540" aria-hidden="true">
    <path d="M0 0H360L362 470L352 488L340 498L300 506L250 512L200 520L150 527L100 532L60 535L20 528L0 522Z" fill="var(--orange)"/>
  </svg>
  <svg class="abs ribbon" viewBox="0 0 200 60" aria-hidden="true">
    <path d="M2 42L30 24L40 20C90 26 150 18 198 2C188 22 170 34 150 40C110 52 60 56 22 52Z" fill="var(--paper)"/>
  </svg>
  <h1 class="abs build-title">
    <span class="line1">BUILD YOUR</span>
    <span class="line2">OWN</span>
    <span class="script">Meal</span>
  </h1>
  <div class="abs price-disc"><span class="price">$8.00</span></div>

  <section class="abs step" style="top:219px">
    <h3>PICK BOWL/ WRAP</h3>
    <p>Salad Bowl, Basmati Rice Bowl, Curry Rice Bowl, Paratha Wrap.</p>
  </section>
  <section class="abs step" style="top:283px">
    <h3>PICK MAIN CURRY OPTION</h3>
    <p>Veg Korma, Chana Masala, CTM, Chili Chicken, Tandoori Chicken</p>
    <p class="extras"><span>Beef Curry +$1</span><span>Goat Curry $2</span><span>Double Protein $2</span></p>
    <p class="note">*(For premium curry extra)</p>
  </section>
  <section class="abs step" style="top:361px; width:300px">
    <h3>PICK TOPPINGS</h3>
    <p>Beets Thoran, Green Beans Thoran, Cabbage Thoran, Chick Pea Salad, Cucumber Salad, diced Onion, chopped bell pepper, shredded Cheese, cilantro, jalapeno</p>
  </section>
  <section class="abs step" style="top:443px; width:320px">
    <h3>PICK SAUCES</h3>
    <p>Original Mint, Sweet Tamarind, Cool Yogurt, Mango Chilli, Tikka Masala</p>
  </section>

  <div class="abs brand-backdrop" role="img" aria-label="Soft peach floral mandala pattern behind the restaurant name"></div>
  <div class="abs brand">Saffron<br>Lane</div>

  <h2 class="abs feature-title">Chicken Biriyani Bowl</h2>
  <span class="abs price feature-price">$7.00</span>
  <p class="abs feature-quote">“The Original Indian Rice Bowl! Chicken and rice which has been baked to perfection.”</p>
  <p class="abs feature-serve">Served with yogurt sauce, pickle and pappadom.</p>
  <svg class="abs hatch" viewBox="0 0 240 24" aria-hidden="true">
    <path class="stroke" stroke-width="2.6" d="M4 21L8 3M11 21L15 3M18 21L22 3M25 21L29 3M32 21L36 3M39 21L43 3M46 21L50 3M53 21L57 3M60 21L64 3M67 21L71 3M74 21L78 3M81 21L85 3M88 21L92 3M95 21L99 3M102 21L106 3M109 21L113 3M116 21L120 3M123 21L127 3M130 21L134 3M137 21L141 3M144 21L148 3M151 21L155 3M158 21L162 3M165 21L169 3M172 21L176 3M179 21L183 3M186 21L190 3M193 21L197 3M200 21L204 3M207 21L211 3M214 21L218 3M221 21L225 3M228 21L232 3"/>
  </svg>
  <div class="abs photo-bowl" role="img" aria-label="Photo of chicken biriyani in a foil bowl on a white plate"></div>
  <div class="abs photo-snack" role="img" aria-label="Photo of samosas with green chutney on a white plate"></div>

  <h2 class="abs section-head snacks-head">SNACKS</h2>
  <svg class="abs swash" viewBox="0 0 110 28" aria-hidden="true">
    <path class="stroke" d="M2 14C30 20 60 4 96 10C106 12 106 22 98 20" stroke-width="4"/>
  </svg>
  <ul class="abs list snacks">
    <li>Samosa<span class="amt">$ 1</span></li>
    <li>Veg Puffs<span class="amt">$ 1.49</span></li>
    <li>Egg Puffs<span class="amt">$ 2.49</span></li>
    <li>Sweet Puffs<span class="amt">$ 1.49</span></li>
    <li>Beef Puffs<span class="amt">$ 1.49</span></li>
    <li>Chicken Puffs<span class="amt">$ 1.49</span></li>
  </ul>

  <h2 class="abs fries-band">LOADED FRIES</h2>
  <svg class="abs" style="left:826px;top:428px;width:46px;height:44px" viewBox="0 0 46 44" aria-hidden="true">
    <path class="stroke" stroke-width="4" d="M3 4C18 10 28 24 34 40M22 4C30 12 36 22 42 30"/>
  </svg>
  <ul class="abs list fries">
    <li>Chicken Tikka Fries</li>
    <li>Tandoori Fries</li>
    <li>Chili Chicken Fries</li>
  </ul>
  <div class="abs fries-disc"><span class="price">$7.00</span></div>

  <h2 class="abs drinks-head">DRINKS</h2>
  <ul class="abs list drinks-a">
    <li>Iced Tea 32oz<span class="amt">2</span></li>
    <li>Lemonade 32oz<span class="amt">2</span></li>
    <li>Masala Tea<span class="amt">2</span></li>
  </ul>
  <ul class="abs list drinks-b">
    <li>Indian Coffee<span class="amt">2</span></li>
    <li>Soda Can<span class="amt">1</span></li>
    <li>Water Bottle<span class="amt">1</span></li>
  </ul>

  <svg class="abs" style="left:832px;top:734px;width:54px;height:68px" viewBox="0 0 54 68" aria-hidden="true">
    <path class="stroke" stroke-width="3.5" d="M4 64C18 40 30 20 44 4M14 60C26 42 38 24 50 10"/>
  </svg>
  <h2 class="abs desserts-head">Desserts</h2>
  <ul class="abs list desserts">
    <li>Mango Pudding<span class="amt">$ 3.50</span></li>
    <li>Rice Pudding<span class="amt">$ 3.50</span></li>
  </ul>

  <svg class="abs" style="left:10px;top:550px;width:56px;height:88px" viewBox="0 0 56 88" aria-hidden="true">
    <path class="stroke" stroke-width="3" d="M52 4C34 24 42 60 2 86M30 10C22 22 24 40 14 56"/>
  </svg>
  <svg class="abs" style="left:250px;top:522px;width:82px;height:38px" viewBox="0 0 82 38" aria-hidden="true">
    <path class="stroke" stroke-width="4" d="M4 22L10 32M18 10L20 34M30 4L30 30M42 12L36 30M56 18L44 34M76 24L56 36"/>
  </svg>
  <h2 class="abs section-head lassi-head">Lassi/ Indian Shakes</h2>
  <div class="abs lassi-cols"><span style="left:0">S</span><span style="left:57px">L</span></div>
  <ul class="abs list lassi">
    <li>Original Lassi<span class="amt s">2</span><span class="amt l">2.5</span></li>
    <li>Mango Lassi<span class="amt s">2.5</span><span class="amt l">3</span></li>
    <li>Rose Lassi<span class="amt s">2.5</span><span class="amt l">3</span></li>
    <li>Chai Spice Lassi<span class="amt s">2.75</span><span class="amt l">3.25</span></li>
    <li>Cookies N Cream Lassi<span class="amt s">2.75</span><span class="amt l">3.25</span></li>
    <li>Chocolate Hazelnut Lassi<span class="amt s">2.75</span><span class="amt l">3.25</span></li>
  </ul>

  <svg class="abs rays" viewBox="0 0 304 80" aria-hidden="true">
    <g class="stroke" stroke-width="5">
      <path d="M16 28L44 38M4 48H42M20 68L44 56M40 8L48 20"/>
      <path d="M288 28L260 38M300 48H262M284 68L260 56M264 8L256 20"/>
    </g>
  </svg>
  <h2 class="abs meals-head"><span class="script">Chicken</span><span class="block">MEALS</span></h2>
  <svg class="abs" style="left:358px;top:724px;width:46px;height:70px" viewBox="0 0 46 70" aria-hidden="true">
    <path class="stroke" stroke-width="4" d="M42 4C26 14 10 28 4 40M34 18C22 28 12 38 8 50M28 36C20 42 14 50 12 58M22 56L14 66"/>
  </svg>
  <ul class="abs list meals">
    <li>Tandoori Chicken /Fries</li>
    <li>Chicken Tender/ Fries</li>
    <li>Spicy Chicken Tender/ Fries</li>
  </ul>
  <div class="abs meals-disc"><span class="price">$7.00</span></div>

</main>
</body>
</html>
```